Vardek Hub, LLC. is the name of the company that will be an Internet startup working in E-commerce and

We are a new company and going to start the business by hiring people we need. We are on “Hiring Now…” status right now which we like to be displayed on the website homepage.
The website should allow us to start the hiring process with letting people see and apply for jobs posted on the website.

the company logo is attached.

Target Market(s)

Tech Job Seekers, Programmers, iOS and Android Developers, Software engineers, Graphic designers, QA engineers, Customer Service Reps,...

Industry/Entity Type

Internet

Number of Pages Required

5+ page

Font styles to use
Serif
Sans Serif

Colors

Designer to choose colors to be used in the design.

Requirements
Must have
• We need a system to help job seekers to upload the resume and cover letter and fill the required forms and answer some questions on a form designed to evaluate the job seekers and let them know if they fit in the position and should apply for it.
• We also want job seekers to do a Pre-Employment Tests including Aptitude, Personality, and Skills after they qualified for a job which links our website to web-based pre-employment testing services websites like (Quorva, Pellmark, Brumhall & Associates, Tolvin Assessment, …)

```html
<!DOCTYPE html>
<html lang="en">
<head>
<meta charset="utf-8">
<title>Vardek Hub — Hiring Now</title>
<link rel="stylesheet" href="https://fonts.googleapis.com/css2?family=Lato:wght@300;400;700&display=swap">
<style>
:root{
  --orange:#ff4f00;
  --orange-soft:#ff8a5c;
  --teal:#2f9fc4;
  --teal-light:#46b8d4;
  --blue-band:#2b88c4;
  --ink:#222;
  --dark:#1b1b1b;
  --footer:#2a2a2a;
  --grey-text:#555;
  --white:#fff;
}
*{box-sizing:border-box;margin:0;padding:0}
html,body{width:1200px;height:3475px;overflow:hidden;background:var(--white);font-family:"Lato",Arial,sans-serif;color:var(--ink)}
.page{position:relative;width:1200px;height:3475px;overflow:hidden}
.abs{position:absolute}

/* header */
.brand{left:0;width:1200px;top:22px;text-align:center;font-size:52px;font-weight:700;color:var(--teal);letter-spacing:1px}
.brand .dot{display:inline-block;width:22px;height:22px;background:var(--orange);margin-left:10px;vertical-align:middle}
.hero-photo{left:0;top:116px;width:1200px;height:591px;background:linear-gradient(120deg,#5c6e80 0%,#9aa6b1 35%,#c9c4bc 60%,#7d7a78 100%)}
.nav{left:76px;top:109px;width:1048px;height:53px;background:var(--orange);box-shadow:0 3px 6px rgba(0,0,0,.35);display:flex;align-items:center}
.nav a{position:absolute;color:var(--white);text-decoration:none;font-size:16px;letter-spacing:.5px}
.nav .active::before{content:"";position:absolute;left:-22px;top:-4px;width:24px;height:24px;border:3px solid var(--white);border-right-color:transparent;border-radius:50%}
.slide-arrow{width:46px;height:34px;background:#4a4a4a;top:400px}
.slide-arrow.left{left:0}
.slide-arrow.right{left:1154px;background:#555}
.hiring-title{right:80px;top:350px;font-size:58px;font-weight:400;color:#111}
.hiring-text{right:80px;top:436px;width:640px;text-align:right;font-size:18px;line-height:25px;color:#111}
.cta-box{left:76px;top:584px;width:313px;height:127px;background:rgba(20,20,20,.85);color:var(--white);text-align:center;font-size:19px;line-height:25px;padding-top:28px}
.cta-btn{left:76px;top:711px;width:313px}
.cta-btn span{position:absolute;left:0;top:14px;width:313px;text-align:center;color:var(--white);font-size:24px;letter-spacing:.5px}

/* stats band */
.stats{left:0;top:707px;width:1200px;height:208px;background:var(--dark)}
.map-area{left:760px;top:720px;width:380px;height:180px;background:radial-gradient(ellipse at center,#3a3a3a 0%,#242424 70%,rgba(27,27,27,0) 100%)}
.job-label{left:619px;top:766px;font-size:34px;font-weight:300;color:var(--white)}
.job-text{left:440px;top:814px;width:313px;text-align:right;font-size:15px;line-height:25px;color:#ddd}
.job-count{left:910px;top:780px;font-size:46px;font-weight:300;color:var(--white)}

/* about */
.team-photo{left:65px;top:968px;width:468px;height:306px;background:linear-gradient(180deg,#f2f2f2 0%,#c8ccd2 60%,#8d939b 100%)}
.about-title{left:581px;top:1038px;font-size:44px;font-weight:400;color:var(--teal)}
.about-title small{font-size:32px}
.about-text{left:581px;top:1098px;width:520px;font-size:14.5px;line-height:25px;color:var(--grey-text)}

/* career */
.career{left:0;top:1274px;width:1200px;height:260px;background:var(--orange);color:var(--white);text-align:center}
.career h2{position:absolute;left:0;width:1200px;top:42px;font-size:40px;font-weight:400}
.career p{position:absolute;left:200px;width:800px;top:94px;font-size:14px;line-height:25px}
.btn{position:absolute;top:174px;height:42px;border-radius:21px;font-size:18px;line-height:40px;color:var(--white);text-align:center}
.btn-fill{left:366px;width:223px;background:var(--orange-soft);border:1px solid #ffd0bb}
.btn-outline{left:605px;width:229px;border:2px solid var(--white)}

/* services */
.section-title{left:0;width:1200px;text-align:center;font-size:44px;font-weight:400;color:var(--teal)}
.section-title .lead{color:var(--teal-light)}
.service{width:260px;text-align:center}
.service svg{display:block;margin:0 auto}
.service span{display:block;margin-top:14px;font-size:20px;color:#333;line-height:26px}

/* tests band */
.tests{left:0;top:1930px;width:1200px;height:572px;background:var(--blue-band)}
.sq-grey{background:#6e6e6e;width:52px;height:50px}
.sq-orange{background:var(--orange);width:62px;height:61px}
.test-card{background:var(--white);border:2px dashed #cfe6f1;outline:6px solid var(--white);text-align:center;font-size:20px;color:var(--teal-light)}
.test-card.skills{color:#f6a07c}
.test-photo{left:707px;top:1925px;width:405px;height:577px;background:linear-gradient(180deg,#4c8fb9 0%,#c5b5a8 45%,#e9e4dc 70%,#2a2a2a 100%);border-radius:40% 40% 0 0}

/* news */
.news-card{top:2618px;height:255px;background:#ececec}
.news-card .img{position:absolute;left:0;top:0;width:100%;height:185px}
.news-card .date{position:absolute;left:0;top:0;width:52px;height:70px;background:var(--white);text-align:center}
.news-card .date b{display:block;font-size:30px;font-weight:400;color:var(--orange);line-height:38px}
.news-card .date i{font-style:normal;font-size:13px;color:#333}
.news-card h3{position:absolute;left:24px;top:198px;font-size:15px;font-weight:700;color:var(--teal)}
.news-card p{position:absolute;left:24px;top:222px;width:250px;font-size:14px;line-height:25px;color:var(--grey-text)}

/* contact */
.contact{left:0;top:2931px;width:1200px;height:417px;background:var(--orange)}
.contact h2{position:absolute;left:0;width:1200px;top:40px;text-align:center;font-size:42px;font-weight:400;color:var(--white)}
.field{position:absolute;background:var(--white);border:3px solid #ffc5ab;font-size:14px;color:#555;padding:8px 10px}
.send{left:680px;top:3203px;width:68px;height:68px;border-radius:50%;background:var(--white);border:3px solid #ffc5ab}
.info{left:846px;width:254px;text-align:center;color:#ffe3d6;font-size:14.5px;line-height:24px}

/* footer */
.footer{left:0;top:3348px;width:1200px;height:127px;background:var(--footer)}
.footer-nav a{position:absolute;top:3372px;font-size:15px;color:var(--white);text-decoration:none}
.footer-nav a.active{color:var(--orange)}
.subscribe{left:776px;top:3361px;width:345px;height:36px;border:2px solid var(--white);border-radius:18px}
.subscribe span{position:absolute;left:20px;top:7px;font-size:14px;color:#f08a5d}
.subscribe b{position:absolute;right:2px;top:2px;width:110px;height:28px;border-radius:14px;background:var(--white);color:var(--orange);font-weight:400;font-size:14px;text-align:center;line-height:28px}
.rule{left:76px;top:3410px;width:1048px;height:1px;background:#555}
.copyright{left:76px;top:3432px;font-size:14px;color:#ddd}
.social{top:3432px;width:18px;height:18px;border-radius:50%;background:#8a8a8a}
</style>
</head>
<body>
<div class="page">

  <!-- header & hero -->
  <div class="abs brand">Vardek Hub<span class="dot"></span></div>
  <div class="abs hero-photo" role="img" aria-label="Photo of two smiling businessmen in suits exchanging a document at an office desk"></div>
  <nav class="abs nav">
    <a class="active" style="left:190px">HOME</a>
    <a style="left:292px">ABOUT</a>
    <a style="left:412px">SERVICES</a>
    <a style="left:548px">CAREER</a>
    <a style="left:670px">NEWS</a>
    <a style="left:780px">CONTACT</a>
  </nav>
  <div class="abs slide-arrow left"><svg width="46" height="34"><path d="M30 17H14M20 11l-6 6 6 6" stroke="#ccc" stroke-width="3" fill="none"/></svg></div>
  <div class="abs slide-arrow right"><svg width="46" height="34"><path d="M16 17h16M26 11l6 6-6 6" stroke="#ff4f00" stroke-width="3" fill="none"/></svg></div>
  <h1 class="abs hiring-title">Hiring Now...</h1>
  <p class="abs hiring-text">Lorem Ipsum is simply dummy text of the printing and typesetting industry, Lorem Ipsum has been the industry's standard.</p>
  <div class="abs cta-box">Looking for a your Aptitude, Personality, and Skills matched job?</div>
  <div class="abs cta-btn">
    <svg width="313" height="80"><polygon points="0,0 313,0 313,60 156,78 0,60" fill="#46b8d4"/></svg>
    <span>CONTACT US</span>
  </div>

  <!-- stats -->
  <div class="abs stats"></div>
  <div class="abs map-area" role="img" aria-label="Dark world map with orange location markers"></div>
  <svg class="abs" style="left:0;top:0" width="1200" height="915" aria-hidden="true">
    <g fill="none" stroke="#ff4f00" stroke-width="2">
      <circle cx="990" cy="738" r="4"/><circle cx="950" cy="763" r="4"/><circle cx="1035" cy="762" r="4"/>
      <circle cx="880" cy="848" r="4"/><circle cx="965" cy="870" r="4"/><circle cx="1065" cy="848" r="4"/>
    </g>
  </svg>
  <div class="abs job-label">job posts</div>
  <p class="abs job-text">Lorem Ipsum is simply dummy text of the printing and typesetting industry.</p>
  <div class="abs job-count">3210</div>

  <!-- about -->
  <div class="abs team-photo" role="img" aria-label="Photo of a smiling business team of five standing together"></div>
  <h2 class="abs about-title">About Vardek <small>HUB</small></h2>
  <p class="abs about-text">Lorem Ipsum is simply dummy text of the printing and typesetting industry. Lorem Ipsum has been the industry's standard dummy text ever since the 1500s, when an unknown printer took a galley of type and scrambled it to make a type specimen book.</p>

  <!-- career -->
  <section class="abs career">
    <h2>Career</h2>
    <p>Lorem Ipsum is simply dummy text of the printing and typesetting industry. Lorem Ipsum has been the industry's standard dummy text ever since the 1500s, when an unknown printer took a galley of type and scrambled it to make a type specimen book.</p>
    <span class="btn btn-fill">upload resume</span>
    <span class="btn btn-outline">Pre-Employment Tests</span>
  </section>

  <!-- services -->
  <h2 class="abs section-title" style="top:1570px"><span class="lead">Our</span> Services</h2>
  <svg width="0" height="0" style="position:absolute">
    <defs>
      <radialGradient id="crescent" cx="40%" cy="40%" r="70%">
        <stop offset="0" stop-color="#ff8a3a"/><stop offset="1" stop-color="#ff4f00"/>
      </radialGradient>
    </defs>
  </svg>
  <div class="abs service" style="left:55px;top:1656px">
    <svg width="160" height="160"><circle cx="80" cy="80" r="78" fill="url(#crescent)"/><circle cx="92" cy="70" r="62" fill="#fff"/>
      <g stroke="#333" stroke-width="3" fill="none"><rect x="72" y="46" width="36" height="56" rx="5"/><circle cx="90" cy="94" r="3"/></g></svg>
    <span>Ios and Android<br>Development</span>
  </div>
  <div class="abs service" style="left:333px;top:1656px">
    <svg width="160" height="160"><circle cx="80" cy="80" r="78" fill="url(#crescent)"/><circle cx="92" cy="70" r="62" fill="#fff"/>
      <g stroke="#333" stroke-width="3" fill="none"><rect x="58" y="44" width="64" height="46" rx="3"/><path d="M82 106h16M90 90v16M76 60l-7 7 7 7M104 60l7 7-7 7M94 56l-8 22"/></g></svg>
    <span>Software Development</span>
  </div>
  <div class="abs service" style="left:604px;top:1656px">
    <svg width="160" height="160"><circle cx="80" cy="80" r="78" fill="url(#crescent)"/><circle cx="92" cy="70" r="62" fill="#fff"/>
      <g stroke="#333" stroke-width="3" fill="none"><rect x="58" y="48" width="64" height="44" rx="3"/><path d="M80 108h20M90 92v16M74 84l30-30 6 6-30 30-8 2z"/></g></svg>
    <span>Web design</span>
  </div>
  <div class="abs service" style="left:873px;top:1656px">
    <svg width="160" height="160"><circle cx="80" cy="80" r="78" fill="url(#crescent)"/><circle cx="92" cy="70" r="62" fill="#fff"/>
      <g stroke="#333" stroke-width="3" fill="none"><path d="M56 62l14-8 20 6 20-6 14 8-10 20-20 14-18-14z"/><path d="M78 72l12 10 8-6"/></g></svg>
    <span>Custom Service</span>
  </div>

  <!-- tests band -->
  <div class="abs tests"></div>
  <svg class="abs" style="left:0;top:1930px" width="760" height="572" aria-hidden="true">
    <path d="M0 180 C120 160 200 260 330 300 S560 420 700 470" stroke="#7fb5d8" stroke-width="2" stroke-dasharray="4 6" fill="none"/>
  </svg>
  <div class="abs sq-grey" style="left:25px;top:1951px"></div>
  <div class="abs sq-grey" style="left:25px;top:2190px"></div>
  <div class="abs sq-orange" style="left:297px;top:1962px"></div>
  <div class="abs test-card" style="left:120px;top:2034px;width:123px;height:123px;line-height:119px">Aptitude</div>
  <div class="abs test-card" style="left:292px;top:2152px;width:144px;height:144px;line-height:140px">Personality</div>
  <div class="abs test-card skills" style="left:487px;top:2289px;width:185px;height:186px;line-height:182px">Skills</div>
  <div class="abs test-photo" role="img" aria-label="Photo of a smiling woman holding a green folder and giving a thumbs up"></div>

  <!-- news -->
  <h2 class="abs section-title" style="top:2540px"><span class="lead">Latest</span> News</h2>
  <article class="abs news-card" style="left:86px;width:310px">
    <div class="img" role="img" aria-label="Photo of a businessman holding a tablet" style="background:linear-gradient(135deg,#3d5660,#8aa0a6)"></div>
    <div class="date"><b>30</b><i>Nov</i></div>
    <h3>Lorem Ipsum is simply dummy...</h3>
    <p>Lorem Ipsum is simply dummy text of the printing and typesetting.</p>
  </article>
  <article class="abs news-card" style="left:445px;width:301px">
    <div class="img" role="img" aria-label="Photo of people reviewing charts at a desk" style="background:linear-gradient(135deg,#6d7b88,#c9ccd0)"></div>
    <div class="date"><b>30</b><i>Nov</i></div>
    <h3>Lorem Ipsum is simply dummy ...</h3>
    <p>Lorem Ipsum is simply dummy text of the printing and typesetting.</p>
  </article>
  <article class="abs news-card" style="left:799px;width:309px">
    <div class="img" role="img" aria-label="Photo of a team meeting around a table" style="background:linear-gradient(135deg,#5a4a40,#b3a595)"></div>
    <div class="date"><b>30</b><i>Nov</i></div>
    <h3>Lorem Ipsum is simply dummy ...</h3>
    <p>Lorem Ipsum is simply dummy text of the printing and typesetting.</p>
  </article>

  <!-- contact -->
  <section class="abs contact">
    <h2>Contact Us</h2>
  </section>
  <div class="field" style="left:79px;top:3077px;width:225px;height:40px">Name</div>
  <div class="field" style="left:324px;top:3077px;width:225px;height:40px">E-mail</div>
  <div class="field" style="left:570px;top:3077px;width:227px;height:40px">Subject</div>
  <div class="field" style="left:79px;top:3137px;width:718px;height:100px;border-radius:6px">Message</div>
  <div class="abs send">
    <svg width="62" height="62"><circle cx="31" cy="31" r="22" fill="#2f9fc4"/><rect x="20" y="23" width="22" height="16" rx="2" fill="#fff"/><path d="M20 24l11 8 11-8" stroke="#2f9fc4" stroke-width="2" fill="none"/></svg>
  </div>
  <svg class="abs" style="left:960px;top:3066px" width="26" height="30"><path d="M13 2a9 9 0 0 1 9 9c0 7-9 17-9 17S4 18 4 11a9 9 0 0 1 9-9z" fill="#fff"/><circle cx="13" cy="11" r="3.5" fill="#ff4f00"/></svg>
  <p class="abs info" style="top:3100px">Lorem Ipsum is simply dummy text<br>of the printing.</p>
  <svg class="abs" style="left:960px;top:3155px" width="26" height="26"><path d="M6 3l5 0 2 6-3 2c1 3 3 5 6 6l2-3 6 2v5c0 1-1 2-2 2C11 23 3 15 3 5c0-1 1-2 3-2z" fill="#fff"/></svg>
  <p class="abs info" style="top:3184px">123 456 7890</p>
  <svg class="abs" style="left:960px;top:3216px" width="26" height="22"><rect x="2" y="3" width="22" height="16" rx="2" fill="none" stroke="#fff" stroke-width="2"/><path d="M3 4l10 8 10-8" stroke="#fff" stroke-width="2" fill="none"/></svg>
  <p class="abs info" style="top:3240px">info@vardekhub.example</p>

  <!-- footer -->
  <footer class="abs footer"></footer>
  <nav class="footer-nav">
    <a class="active" style="left:79px">Home</a>
    <a style="left:158px">About</a>
    <a style="left:240px">Services</a>
    <a style="left:334px">Career</a>
    <a style="left:421px">News</a>
    <a style="left:498px">Contact</a>
  </nav>
  <div class="abs subscribe"><span>Email...</span><b>Subscribe</b></div>
  <div class="abs rule"></div>
  <p class="abs copyright">©Vardek Hub. 2017 - All Rights Reserved.</p>
  <span class="abs social" style="left:982px" aria-label="Social link"></span>
  <span class="abs social" style="left:1014px" aria-label="Social link"></span>
  <span class="abs social" style="left:1048px" aria-label="Social link"></span>
  <span class="abs social" style="left:1100px" aria-label="Social link"></span>

</div>
</body>
</html>
```